Personal Brand Business Card

I am looking for a design that I will use as my personal brand that conveys class (think 1920s gentlemen) and is timeless. I will be putting this on a pearl white, letter pressed, cotton business card.  I’m thinking maybe something with my initials on the front they will flip over for the rest of my information.  But don’t let that limit you.
The information I will have on the back of the business card will be my name, email, and phone number.
Some of the attributes that best describe me are: loyal, dependable, creative, risk taker, open minded, competitive, and empathetic.  I can adapt to my environment quickly and can get along with anyone.  I get excited by figuring out the way things work and finding solutions to problems.

Industry/Entity Type
Business

```html
<!DOCTYPE html>
<html lang="en">
<head>
<meta charset="utf-8">
<title>Grant Whitfield – Business Card</title>
<link rel="stylesheet" href="https://fonts.googleapis.com/css2?family=Tenor+Sans&display=swap">
<style>
  :root {
    --page-bg: #e9e7e3;
    --ink: #111111;
    --card-black: #0e0e0e;
    --card-white: #ffffff;
    --pattern-tone: #f3f3f3;
    --ghost: #1b1b1b;
    --paper-text: #f2f2f2;
    --shadow: rgba(0, 0, 0, 0.18);
  }
  * { margin: 0; padding: 0; box-sizing: border-box; }
  html, body {
    width: 1200px;
    height: 784px;
    overflow: hidden;
    background: var(--page-bg);
    font-family: "Tenor Sans", "Optima", sans-serif;
  }
  .canvas {
    position: relative;
    width: 1200px;
    height: 784px;
    display: flex;
    align-items: center;
    justify-content: center;
    gap: 60px;
  }
  .card {
    position: relative;
    width: 520px;
    height: 298px;
    overflow: hidden;
    box-shadow: 0 8px 24px var(--shadow);
  }

  /* Back of card */
  .card-back {
    background: var(--card-black);
    color: var(--paper-text);
  }
  .card-back .ghost-name {
    position: absolute;
    left: -10px;
    bottom: 18px;
    font-size: 118px;
    line-height: 1;
    color: var(--ghost);
    white-space: nowrap;
    letter-spacing: 2px;
  }
  .card-back .details {
    position: absolute;
    inset: 0;
    display: flex;
    flex-direction: column;
    align-items: center;
    padding-top: 58px;
  }
  .card-back .holder-name {
    font-size: 19px;
    letter-spacing: 5px;
    margin-bottom: 44px;
  }
  .card-back .phone {
    font-size: 17px;
    letter-spacing: 2px;
    margin-bottom: 16px;
  }
  .card-back .email {
    font-size: 14px;
    letter-spacing: 1px;
  }

  /* Front of card */
  .card-front {
    background: var(--card-white);
  }
  .card-front .frame {
    position: absolute;
    inset: 8px;
    border: 2px solid var(--ink);
  }
  .card-front .frame-inner {
    position: absolute;
    inset: 16px;
    border: 9px solid var(--ink);
  }
  .card-front .texture {
    position: absolute;
    inset: 25px;
    background: var(--pattern-tone);
  }
  .card-front .identity {
    position: absolute;
    inset: 25px;
    display: flex;
    flex-direction: column;
    align-items: center;
    justify-content: center;
    color: var(--ink);
  }
  .card-front .brand-name {
    font-size: 58px;
    line-height: 1;
    letter-spacing: 1px;
  }
  .card-front .holder-name {
    font-size: 20px;
    letter-spacing: 5px;
    margin-top: 10px;
  }
</style>
</head>
<body>
  <main class="canvas">
    <section class="card card-back" aria-label="Card back">
      <div class="ghost-name" aria-hidden="true">Whitfield</div>
      <div class="details">
        <p class="holder-name">Grant Whitfield</p>
        <p class="phone">555-014-2873</p>
        <p class="email">grant.whitfield@example.com</p>
      </div>
    </section>

    <section class="card card-front" aria-label="Card front">
      <div class="frame"></div>
      <div class="frame-inner"></div>
      <div class="texture" role="img" aria-label="Fine light grey diamond texture"></div>
      <div class="identity">
        <p class="brand-name">Whitfield</p>
        <p class="holder-name">Grant Whitfield</p>
      </div>
    </section>
  </main>
</body>
</html>
```